Verpackungen für gebrannten Mandeln und Nüsse
Zielgruppe
Wir betreiben eine kleine Süßwarenmanufaktur und stellen Produkte wie Popcorn, Zuckerwatte, Zuckerwattezucker sowie gebrannte Mandeln und Nüsse in den unterschiedlichsten Geschmacksrichtungen selbst her. Unsere Produkte verkaufen wir nahezu nur online, im eigenen Shop und auf zwei weiteren Portalen. Bis auf die Zuckerwatte verpacken wir unsere Produkte im Standbodenbeutel
Aufgabenstellung
Die Verpackung wird in erster Linie für die gebrannten Mandeln und Nüsse benötigt, wenn passend, dann gerne auch für das Popcorn und den Aromazucker. Es sollen später Standbodenbeutel bedruckt werden, die optisch so ansprechend sind, dass Einzelhändler sie sich auch in ihre Regale stellen würden. Andere Geschmacksrichtungen kann man ggf. durch andere Farbtöne darstellen, so dass das Hauptdesign immer gleich bleibt?!
Die Produkte sind vegan und aktuell nutzen wir Standbodenbeutel im braunen Kraftpapier. Es sollte aber nicht zu sehr Öko wirken, sondern mehr Lust auf Knabbern machen. Man kann sich gerne in unserem Shop (www.linas-knabberhof.shop), es muss sich aber nicht an das bisherige Design orientiert werden. Gerne lasse ich mich auch von anderen Designs inspirieren, da ich mit dem jetzigen auch nicht sooo sehr zufrieden bin.
- Vorne ggf. mit Bezeichnung, Geschmacksrichtung, Logo, Produktfoto
- Hinten mit Zutaten, Nährwerttabelle, Barcode, MHD und kurzer Produktbeschreibung sowie Platz für eine kleine Unternehmensbeschreibung.
- Unten kann leer bleiben.
Druckvorlage für die spätere Packungsgröße ist hochgeladen.

```html
<!DOCTYPE html>
<html lang="de">
<head>
<meta charset="utf-8">
<title>Gebrannte Mandeln – Verpackung &amp; Shop</title>
<link rel="stylesheet" href="https://fonts.googleapis.com/css2?family=Yanone+Kaffeesatz:wght@400;700&family=Source+Sans+3:wght@400;600&display=swap">
<style>
  :root {
    --black: #000;
    --stage: #ececec;
    --kraft: #c9a36b;
    --kraft-dark: #b78f57;
    --red: #a03022;
    --blue: #1d9bcb;
    --white: #fff;
    --almond-1: #a5552a;
    --almond-2: #d79a6a;
    --pink: #f848a4;
    --sky: #86d0f0;
    --sky-pale: #e9f4d8;
    --orange: #f07a2a;
    --nav-red: #e0341c;
    --ink: #2c4f63;
    --text: #3a4a55;
  }
  * { box-sizing: border-box; margin: 0; padding: 0; }
  html, body { width: 1125px; height: 1200px; overflow: hidden; background: var(--black); }
  body { position: relative; font-family: "Source Sans 3", sans-serif; }

  .stage { position: absolute; left: 0; top: 28px; width: 1125px; height: 749px; background: var(--stage); }

  .pouch { position: absolute; width: 284px; height: 468px; background: var(--kraft);
    border-radius: 10px 10px 28px 28px; }
  .pouch::before { content: ""; position: absolute; left: 0; right: 0; top: 58px; height: 2px; background: var(--kraft-dark); }
  .pouch--left { left: 202px; top: 172px; }
  .pouch--right { left: 651px; top: 175px; }

  .pouch__label { position: absolute; left: 79px; top: 1px; width: 131px; height: 194px;
    color: var(--white); text-align: center; font-family: "Yanone Kaffeesatz", sans-serif; }
  .pouch__label--red { background: var(--red); }
  .pouch__label--blue { background: var(--blue); }
  .pouch__title { font-weight: 700; font-size: 38px; line-height: 37px; margin-top: 14px; }
  .pouch__flavour { font-weight: 400; font-size: 17px; letter-spacing: 4px; margin-top: 8px; }
  .pouch__brand { display: flex; flex-direction: column; align-items: center; margin-top: 10px; gap: 5px; }
  .pouch__brand-dot { width: 14px; height: 14px; border-radius: 50%; background: var(--white); }
  .pouch__brand-name { font-size: 17px; font-weight: 400; line-height: 17px; }

  .pouch__window { position: absolute; left: 10px; right: 10px; top: 342px; height: 69px;
    background: linear-gradient(100deg, var(--almond-1), var(--almond-2) 30%, var(--almond-1) 55%, var(--almond-2) 80%, var(--almond-1)); }

  .shop { position: absolute; left: 91px; top: 845px; width: 900px; height: 305px; overflow: hidden;
    background: linear-gradient(180deg, var(--sky) 0%, var(--sky) 45%, var(--sky-pale) 100%); }
  .shop__promo { height: 23px; background: var(--pink); color: var(--white); font-size: 9px;
    text-align: center; line-height: 23px; }

  .shop__logo { position: absolute; left: 75px; top: 35px; display: flex; align-items: center; gap: 8px; }
  .shop__logo-dot { width: 22px; height: 22px; border-radius: 50%; background: var(--pink); }
  .shop__logo-name { font-family: "Yanone Kaffeesatz", sans-serif; font-weight: 700; font-size: 30px; color: var(--pink); }

  .shop__account { position: absolute; left: 672px; top: 32px; width: 143px; height: 16px;
    background: rgba(255,255,255,.85); border-radius: 8px; display: flex; justify-content: space-around;
    align-items: center; font-size: 9px; color: var(--orange); }
  .shop__search { position: absolute; left: 658px; top: 68px; width: 30px; height: 30px; }
  .shop__cart { position: absolute; left: 713px; top: 55px; width: 107px; height: 52px; }

  .shop__nav { position: absolute; left: 78px; top: 124px; width: 744px; height: 25px; border-radius: 12px;
    background: linear-gradient(90deg, #bfe7f3, #fbfbe8 50%, #bfe7f3); display: flex; justify-content: center;
    align-items: center; font-family: "Yanone Kaffeesatz", sans-serif; font-size: 12px; font-weight: 700; color: var(--orange); }
  .shop__nav span { padding: 0 7px; border-left: 1px solid rgba(0,0,0,.08); }
  .shop__nav span:first-child { border-left: none; }
  .shop__nav .is-active { color: var(--nav-red); }

  .shop__panel { position: absolute; left: 78px; top: 158px; width: 744px; height: 160px;
    background: rgba(255,255,255,.35); border-radius: 8px; }
  .shop__side { position: absolute; left: 9px; top: 10px; width: 167px; }
  .shop__side div { height: 24px; margin-bottom: 2px; border-radius: 5px; background: #6cc3ec;
    color: var(--white); font-family: "Yanone Kaffeesatz", sans-serif; font-weight: 700; font-size: 12px;
    line-height: 24px; padding-left: 12px; }
  .shop__main { position: absolute; left: 195px; top: 10px; width: 540px; }
  .shop__heading { font-family: "Yanone Kaffeesatz", sans-serif; font-weight: 700; font-size: 24px;
    color: var(--ink); border-bottom: 1px solid #c9dfe2; padding-bottom: 2px; }
  .shop__intro { font-size: 9px; line-height: 14px; color: var(--text); margin-top: 11px; }
  .shop__sort { position: absolute; left: 420px; top: 81px; font-size: 9.5px; color: var(--text); }
  .shop__select { margin-top: 3px; width: 120px; height: 22px; background: var(--white); border: 1px solid #9ab;
    border-radius: 3px; font-size: 9.5px; line-height: 20px; padding-left: 6px; position: relative; }
  .shop__select::after { content: "⌄"; position: absolute; right: 6px; top: -3px; }
  .shop__count { font-size: 7.5px; color: var(--ink); text-align: right; margin-top: 4px; }
</style>
</head>
<body>
  <section class="stage">
    <div class="pouch pouch--left">
      <div class="pouch__label pouch__label--red">
        <div class="pouch__title">Gebrannte<br>Mandeln</div>
        <div class="pouch__flavour">ZIMT &amp; KAKAO</div>
        <div class="pouch__brand"><span class="pouch__brand-dot"></span><span class="pouch__brand-name">Linas Knabberhof</span></div>
      </div>
      <div class="pouch__window" role="img" aria-label="Sichtfenster mit gebrannten Mandeln"></div>
    </div>
    <div class="pouch pouch--right">
      <div class="pouch__label pouch__label--blue">
        <div class="pouch__title">Gebrannte<br>Mandeln</div>
        <div class="pouch__flavour">KAKAO &amp; VANILLE</div>
        <div class="pouch__brand"><span class="pouch__brand-dot"></span><span class="pouch__brand-name">Linas Knabberhof</span></div>
      </div>
      <div class="pouch__window" role="img" aria-label="Sichtfenster mit gebrannten Mandeln"></div>
    </div>
  </section>

  <section class="shop">
    <div class="shop__promo">Newsletter abonnieren = 10% Rabatt für Dich</div>
    <div class="shop__logo"><span class="shop__logo-dot"></span><span class="shop__logo-name">Linas Knabberhof</span></div>
    <div class="shop__account"><span>Einloggen</span><span>Konto erstellen</span></div>
    <svg class="shop__search" viewBox="0 0 30 30" aria-label="Suche">
      <circle cx="15" cy="15" r="15" fill="#f39a1a"/>
      <circle cx="14" cy="14" r="5" fill="none" stroke="#fff" stroke-width="2"/>
      <line x1="17.5" y1="17.5" x2="21" y2="21" stroke="#fff" stroke-width="2.4" stroke-linecap="round"/>
    </svg>
    <svg class="shop__cart" viewBox="0 0 107 52" aria-label="Warenkorb">
      <path d="M12 44 Q0 44 4 34 Q8 26 18 28 Q20 14 36 16 Q44 4 60 10 Q72 6 78 18 Q94 16 96 28 Q107 30 102 40 Q100 46 90 46 Z" fill="#fff"/>
      <path d="M44 14 h4 l3 9 h9 l2 -7 h-13" fill="none" stroke="#8fb6c6" stroke-width="1.3"/>
      <text x="45" y="40" font-family="Source Sans 3, sans-serif" font-size="18" fill="#2a7fa8">0</text>
      <text x="60" y="32" font-family="Source Sans 3, sans-serif" font-size="5" fill="#2a7fa8">Produkte</text>
      <text x="60" y="37" font-family="Source Sans 3, sans-serif" font-size="5" fill="#2a7fa8">im</text>
      <text x="60" y="42" font-family="Source Sans 3, sans-serif" font-size="5" fill="#2a7fa8">Warenkorb</text>
    </svg>
    <nav class="shop__nav"><span>Home</span><span>Popcorn</span><span>Zuckerwatte</span><span>Gebranntes</span><span class="is-active">Aromazucker</span><span>Bonbons</span></nav>
    <div class="shop__panel">
      <div class="shop__side">
        <div>Home</div><div>Popcorn</div><div>Zuckerwatte</div><div>Gebranntes</div><div>Aromazucker</div><div></div>
      </div>
      <div class="shop__main">
        <h1 class="shop__heading">Aromazucker</h1>
        <p class="shop__intro">Einfach unseren veganen Aromazucker in die Zuckerwattemaschine geben und sich über bunte Zuckerwatte in den unterschiedlichsten Geschmacksrichtungen freuen.</p>
        <div class="shop__sort">Sortieren nach:
          <div class="shop__select">meistverkauft</div>
          <div class="shop__count">16 Produkte</div>
        </div>
      </div>
    </div>
  </section>
</body>
</html>
```